Brackwell Immigration Law

We need a web design for our existing company www.brackwellcounselpartners.co.uk. We are an immigration consultancy. The final design should communicate professionalism, integrity and affordability.

Industry/Entity Type

It Company

Logo Text

Brackwell Counsel Partners

Number of Pages Required

5+ page

Font styles to use
Serif

Requirements
Must have
• I want to have the same silhouette logo but something different in positioning..
Nice to have
• Please have a look at these websites:
• https://www.tenderpathguide.co.uk/visa_uk/
• http://www.moorgatelegal.co.uk/
• http://www.quillfieldcounsel.org/index.php
• www.brackwellcounselpartners.co.uk

```html
<!DOCTYPE html>
<html lang="en">
<head>
<meta charset="utf-8">
<title>Brackwell Counsel Partners — Immigration Law</title>
<link rel="stylesheet" href="https://fonts.googleapis.com/css2?family=Open+Sans:wght@400;600;700;800&display=swap">
<style>
:root{
  --accent:#f7a600;
  --ink:#333333;
  --muted:#777777;
  --white:#ffffff;
  --light:#efefef;
  --footer:#3b3b3b;
  --card-border:#e2e2e2;
}
*{box-sizing:border-box;margin:0;padding:0}
html,body{width:1200px;height:2960px;overflow:hidden}
body{font-family:"Open Sans",Arial,sans-serif;color:var(--ink);background:var(--white)}
.page{position:relative;width:1200px;height:2960px}
section,header,footer{position:absolute;left:0;width:1200px}

/* hero */
.hero{top:0;height:600px;overflow:hidden}
.hero-photo{position:absolute;inset:0;background:linear-gradient(100deg,#3c4a55 0%,#5a6670 35%,#8a8f93 60%,#6d7378 100%)}
.hero-shade{position:absolute;inset:0;background:rgba(20,24,28,.35)}
.topbar{position:absolute;top:28px;left:160px;right:160px;display:flex;justify-content:space-between;align-items:flex-start}
.brand{color:var(--white);font-weight:700;font-size:15px;letter-spacing:.5px;line-height:1.35;display:flex;gap:10px;align-items:flex-start}
.brand-mark{width:12px;height:12px;background:var(--white);margin-top:4px}
.brand small{display:block;font-size:12px;font-weight:700}
.nav{display:flex;gap:30px;list-style:none}
.nav li{color:var(--white);font-size:13px;font-weight:600;letter-spacing:.6px}
.hero-title{position:absolute;top:238px;left:0;right:0;text-align:center;color:var(--white);font-weight:800;font-size:44px;line-height:56px;text-transform:uppercase}
.hero-title .hl{color:var(--accent)}
.btn-outline{position:absolute;top:382px;left:520px;width:160px;height:46px;border:2px solid var(--white);color:var(--white);font-size:14px;font-weight:600;letter-spacing:1px;display:flex;align-items:center;justify-content:center}

/* headings */
.section-title{text-align:center;font-weight:700;font-size:24px;letter-spacing:1px;text-transform:uppercase}

/* about */
.about{top:600px;height:230px;padding-top:56px}
.about p{width:620px;margin:32px auto 0;text-align:center;color:var(--muted);font-size:14px;line-height:24px}

/* services */
.services{top:830px;height:490px;overflow:hidden}
.services-photo{position:absolute;inset:0;background:linear-gradient(180deg,#2a2b2f 0%,#17181a 60%,#242528 100%)}
.services .section-title{position:relative;color:var(--white);margin-top:56px}
.service-grid{position:absolute;top:118px;left:160px;width:880px;display:grid;grid-template-columns:repeat(4,200px);column-gap:26px;row-gap:40px}
.service{height:124px;border:1px solid rgba(255,255,255,.55);color:var(--white);font-size:12px;font-weight:600;letter-spacing:.5px;text-transform:uppercase;display:flex;align-items:center;justify-content:center;text-align:center;padding:0 16px;line-height:18px}
.service.active{background:var(--accent);border-color:var(--accent)}

/* team */
.team{top:1320px;height:740px;padding-top:48px}
.team-grid{position:absolute;top:112px;left:160px;width:880px;display:grid;grid-template-columns:repeat(3,272px);column-gap:32px}
.member-photo{height:368px;border:1px solid var(--card-border)}
.member:nth-child(1) .member-photo{background:linear-gradient(180deg,#f4f4f4,#cfc6bd)}
.member:nth-child(2) .member-photo{background:linear-gradient(180deg,#f4f4f4,#3a3c40)}
.member:nth-child(3) .member-photo{background:linear-gradient(180deg,#f4f4f4,#b9424a)}
.member h3{color:var(--accent);font-size:20px;font-weight:700;margin-top:30px}
.member p{color:var(--muted);font-size:13px;line-height:21px;margin-top:12px}

/* testimonials */
.testimonials{top:2060px;height:260px;background:var(--light);padding-top:40px}
.quote{width:720px;margin:40px auto 0;text-align:center;color:var(--muted);font-size:13px;line-height:21px;font-style:italic}
.quote-author{text-align:center;color:var(--muted);font-size:12px;margin-top:26px}
.arrow{position:absolute;top:120px}
.arrow.left{left:166px}.arrow.right{right:166px}

/* news */
.news{top:2320px;height:500px;padding-top:56px}
.news-grid{position:absolute;top:108px;left:160px;width:880px;display:grid;grid-template-columns:repeat(3,276px);column-gap:26px}
.post{height:332px;background:var(--white);border:1px solid var(--card-border)}
.post-image{height:192px}
.post:nth-child(1) .post-image{background:linear-gradient(135deg,#f7b500,#e79800)}
.post:nth-child(2) .post-image{background:linear-gradient(180deg,#7c8a96,#5a5e62 60%,#c9a017)}
.post:nth-child(3) .post-image{background:linear-gradient(135deg,#cfd3d6,#8f8a83)}
.post-body{padding:14px 18px}
.post h4{font-size:13px;font-weight:600;line-height:19px;color:var(--ink)}
.post:nth-child(1) h4{color:var(--accent)}
.post p{font-size:11px;line-height:17px;color:var(--muted);margin-top:8px}
.read-more{display:block;font-size:11px;font-weight:700;color:var(--ink);margin-top:12px;letter-spacing:.5px}

/* footer */
.site-footer{top:2820px;height:140px;background:var(--footer)}
.site-footer .brand{position:absolute;top:48px;left:160px}
.social{position:absolute;top:60px;right:160px;display:flex;gap:18px}
.social span{width:20px;height:20px;border-radius:50%;background:#cfcfcf;display:block}
</style>
</head>
<body>
<div class="page">

<header class="hero">
  <div class="hero-photo" role="img" aria-label="Photograph of a smiling student sitting in a bright university hallway with other students walking behind"></div>
  <div class="hero-shade"></div>
  <div class="topbar">
    <div class="brand"><span class="brand-mark"></span><div>BRACKWELL COUNSEL PARTNERS<small>IMMIGRATION LAW</small></div></div>
    <ul class="nav"><li>HOME</li><li>ABOUT US</li><li>SERVICES</li><li>TEAM</li><li>CONTACT</li></ul>
  </div>
  <h1 class="hero-title"><span class="hl">Immigration Law</span> was<br>never easy before</h1>
  <div class="btn-outline">CONTACT US</div>
</header>

<section class="about">
  <h2 class="section-title">About Us</h2>
  <p>Brackwell Counsel Partners is regulated by the Immigration Advice Standards Board (IASB) and we have built our reputation on good quality legal work delivered at a fair and affordable price for every client.</p>
</section>

<section class="services">
  <div class="services-photo" role="img" aria-label="Photograph of graduation caps thrown into the air against a dark background"></div>
  <h2 class="section-title">Immigration Law</h2>
  <div class="service-grid">
    <div class="service">Entry Clearance Visitors Visa</div>
    <div class="service">Immigration Appeals</div>
    <div class="service active">Settlement / Naturalisation</div>
    <div class="service">Domestic Workers Visa</div>
    <div class="service">Student Visa</div>
    <div class="service">Work Permits</div>
    <div class="service">Asylum</div>
    <div class="service">Immigration Detention</div>
  </div>
</section>

<section class="team">
  <h2 class="section-title">Our Team</h2>
  <div class="team-grid">
    <article class="member">
      <div class="member-photo" role="img" aria-label="Portrait photo of a female attorney in glasses and a light sweater"></div>
      <h3>ATTORNEY 1</h3>
      <p>I'm a paragraph. Click here to add your own text and edit me. It's easy. Just click "Edit Text" or double click me and you can start adding your own content and make changes to the font.</p>
    </article>
    <article class="member">
      <div class="member-photo" role="img" aria-label="Portrait photo of a male attorney in a dark suit with arms crossed"></div>
      <h3>ATTORNEY 1</h3>
      <p>I'm a paragraph. Click here to add your own text and edit me. It's easy. Just click "Edit Text" or double click me and you can start adding your own content and make changes to the font.</p>
    </article>
    <article class="member">
      <div class="member-photo" role="img" aria-label="Portrait photo of a female attorney in a waistcoat holding a red folder"></div>
      <h3>ATTORNEY 1</h3>
      <p>I'm a paragraph. Click here to add your own text and edit me. It's easy. Just click "Edit Text" or double click me and you can start adding your own content and make changes to the font.</p>
    </article>
  </div>
</section>

<section class="testimonials">
  <h2 class="section-title">Testimonials</h2>
  <svg class="arrow left" width="12" height="20" viewBox="0 0 12 20"><path d="M10 2 2 10l8 8" fill="none" stroke="#999" stroke-width="2"/></svg>
  <svg class="arrow right" width="12" height="20" viewBox="0 0 12 20"><path d="M2 2l8 8-8 8" fill="none" stroke="#999" stroke-width="2"/></svg>
  <p class="quote">"I was a Tier 4 Student studying at a college in East London. When the college lost its sponsorship licence, the team guided me through every step, kept me calm and secured my new visa quickly and at a price I could afford."</p>
  <p class="quote-author">Daniel Reyes, Student</p>
</section>

<section class="news">
  <h2 class="section-title">Latest News</h2>
  <div class="news-grid">
    <article class="post">
      <div class="post-image" role="img" aria-label="Bright yellow abstract image with geometric shapes"></div>
      <div class="post-body">
        <h4>Changes to the Tier 4 visa rules announced this month</h4>
        <p>A short summary of the latest rule changes and what they mean for students planning to study in the UK this year.</p>
        <span class="read-more">READ MORE</span>
      </div>
    </article>
    <article class="post">
      <div class="post-image" role="img" aria-label="Photograph of a yellow taxi on a busy city street"></div>
      <div class="post-body">
        <h4>Fifteen ways we can help you make a smooth transition</h4>
        <p>Practical advice for families relocating, from first application to settling into your new home and work.</p>
        <span class="read-more">READ MORE</span>
      </div>
    </article>
    <article class="post">
      <div class="post-image" role="img" aria-label="Photograph of two people looking surprised in front of a pale wall"></div>
      <div class="post-body">
        <h4>How you can move to workers at work</h4>
        <p>Guidance for employers sponsoring skilled workers, including licences, duties and common mistakes to avoid.</p>
        <span class="read-more">READ MORE</span>
      </div>
    </article>
  </div>
</section>

<footer class="site-footer">
  <div class="brand"><span class="brand-mark"></span><div>BRACKWELL COUNSEL PARTNERS<small>IMMIGRATION LAW</small></div></div>
  <div class="social"><span></span><span></span></div>
</footer>

</div>
</body>
</html>
```